Stationery Design Project - KLVA Partners

Business Cards
Size: 90mm x 55mm
Letterhead
Size: A4 - 210mm x 297mm
With Compliments Slip
Size: DL - 210mm x 99mm
Presentation Folder
Size: A4

KLVA Partners
website: www.klvapartners.com.au (Under construction)
Offices: *Perth *Brisbane * Seoul

A company that supply Safety consultantcy services

Industry/Entity Type

Business

```html
<!DOCTYPE html>
<html lang="en">
<head>
<meta charset="utf-8">
<title>KLVA Partners – Stationery</title>
<link rel="stylesheet" href="https://fonts.googleapis.com/css2?family=Exo+2:wght@300;400&family=PT+Sans:wght@400&display=swap">
<style>
  :root {
    --backdrop: #c9c9c9;
    --paper: #ffffff;
    --brand-dark: #0a5f9a;
    --brand-mid: #4a93c6;
    --brand-light: #8ecbee;
    --ink: #222222;
    --ink-sign: #dfe6f3;
    --logo: #2f80c0;
  }
  * { margin: 0; padding: 0; box-sizing: border-box; }
  html, body { width: 1200px; height: 900px; overflow: hidden; }
  body { background: var(--backdrop); position: relative; font-family: "PT Sans", Tahoma, sans-serif; color: var(--ink); }

  .sheet { position: absolute; background: var(--paper); overflow: hidden; }
  .band { position: absolute; left: 0; top: 0; width: 100%; height: 100%; }
  .wordmark { position: absolute; display: flex; align-items: center; gap: 8px;
    font-family: "Exo 2", sans-serif; font-weight: 300; color: var(--logo); white-space: nowrap; }
  .wordmark .mark { background: var(--logo); display: block; }
  .contact { position: absolute; font-family: "Exo 2", sans-serif; font-weight: 300; color: #fff; text-align: right; white-space: nowrap; }

  /* Letterhead */
  .letterhead { left: 123px; top: 50px; width: 566px; height: 800px; z-index: 1; }
  .letterhead .wordmark { left: 47px; top: 58px; font-size: 26px; }
  .letterhead .wordmark .mark { width: 50px; height: 50px; }
  .recipient { position: absolute; left: 64px; top: 173px; font-size: 10.5px; line-height: 15.5px; font-style: normal; }
  .salutation { position: absolute; left: 64px; top: 234px; font-size: 10.5px; }
  .letter-body { position: absolute; left: 64px; top: 265px; width: 447px; font-size: 10px; line-height: 15px; }
  .letter-body p + p { margin-top: 15px; }
  .letter-body .line { display: block; white-space: nowrap; text-align: justify; text-align-last: justify; }
  .letter-body .line.last { text-align-last: left; }
  .signature { position: absolute; left: 60px; top: 573px; width: 165px; height: 44px; background: var(--ink-sign); }
  .sign-off { position: absolute; left: 64px; top: 614px; font-size: 10.5px; line-height: 16px; }
  .letterhead .contact { right: 30px; top: 747px; font-size: 8.5px; line-height: 11.5px; }

  /* With compliments slip */
  .comp-slip { left: 514px; top: 152px; width: 565px; height: 265px; z-index: 2; }
  .comp-slip .wordmark { left: 36px; top: 33px; font-size: 25px; }
  .comp-slip .wordmark .mark { width: 50px; height: 50px; }
  .comp-title { position: absolute; right: 25px; top: 50px; font-family: "Exo 2", sans-serif; font-weight: 400; font-size: 13px; color: var(--brand-dark); letter-spacing: .2px; }
  .comp-slip .contact { right: 26px; top: 216px; font-size: 8px; line-height: 11px; }

  /* Business card front */
  .card-front { left: 757px; top: 467px; width: 243px; height: 147px; }
  .card-front .wordmark { left: 25px; top: 32px; font-size: 17px; gap: 6px; }
  .card-front .wordmark .mark { width: 34px; height: 34px; }
  .offices { position: absolute; right: 15px; top: 128px; font-family: "Exo 2", sans-serif; font-weight: 300; font-size: 7.5px; color: #fff; letter-spacing: .5px; }

  /* Business card back */
  .card-back { left: 757px; top: 636px; width: 243px; height: 147px; background: var(--brand-dark); color: #fff; }
  .card-art { position: absolute; left: 88px; top: 8px; width: 155px; height: 100px; background: linear-gradient(160deg, var(--brand-mid), var(--brand-dark)); }
  .holder-name { position: absolute; left: 16px; top: 41px; font-family: "Exo 2", sans-serif; font-weight: 400; font-size: 9.5px; letter-spacing: .3px; }
  .holder-role { position: absolute; left: 16px; top: 54px; font-family: "Exo 2", sans-serif; font-weight: 300; font-size: 6.5px; }
  .card-rule { position: absolute; left: 16px; right: 14px; top: 113px; border-top: 1px solid rgba(255,255,255,.35); }
  .card-back .contact { left: 16px; right: 14px; top: 119px; font-size: 6.3px; line-height: 10px; text-align: left; }
</style>
</head>
<body>

<section class="sheet letterhead">
  <div class="wordmark"><span class="mark"></span>KLVA Partners</div>
  <address class="recipient">Laura Benton<br>48 Orchard Lane<br>Milford MA</address>
  <p class="salutation">Dear Mrs Laura Benton,</p>
  <div class="letter-body">
    <p>
      <span class="line">Lorem ipsum dolor sit amet, consectetur adipiscing elit. Integer aliquam nibh vitae</span>
      <span class="line">consectetur et id orci. Praesent vitae felis vitae justo elementum blandit in</span>
      <span class="line">turpis semper dui elementum nec aliquet lectus pulvinar. Donec condimentum</span>
      <span class="line">congue risus congue a. Maecenas commodo, nisi a gravida mollis, lorem erat</span>
      <span class="line">condimentum leo, in pellentesque elit erat id nisi. Pellentesque congue tempus</span>
      <span class="line">Nam tincidunt viverra elit at hendrerit. Quisque eget purus tellus. Mauris faucibus</span>
      <span class="line last">pulvinar consectetur.</span>
    </p>
    <p>
      <span class="line">Nunc molestie iaculis orci, vitae consequat mi condimentum vitae. Etiam et tortor velit. Sed ac</span>
      <span class="line">magna tellus. Proin quam augue, vehicula sed euismod in, vehicula eu felis. Pellentesque a</span>
      <span class="line">orci ac turpis commodo varius at ut arcu. Integer viverra semper sapien fermentum egestas.</span>
      <span class="line">Curabitur erat purus, congue et faucibus sit amet, fringilla elementum odio. Sed pretium</span>
      <span class="line">tincidunt mi, nec fermentum urna interdum sed. Nam et lectus turpis, quis cursus ipsum.</span>
      <span class="line last">Maecenas non nibh odio. Sed in laoreet justo.</span>
    </p>
    <p>
      <span class="line">Aenean sed sem lacus. Vivamus auctor, sapien non aliquet ultrices, mauris turpis porttitor nisl,</span>
      <span class="line">id rutrum velit erat non urna. Praesent eu augue eu ligula feugiat malesuada. Proin nec nibh</span>
      <span class="line">erat. Sed et leo id leo volutpat viverra non ac mi. In quis dictum magna. Donec ut dui sed dui</span>
      <span class="line last">tristique dictum. Donec varius sapien sed turpis dictum a dignissim diam facilisis.</span>
    </p>
  </div>
  <div class="signature" role="img" aria-label="Handwritten signature of Daniel Reeves"></div>
  <p class="sign-off">Yours Sincerely<br>Daniel Reeves</p>
  <svg class="band" viewBox="0 0 566 800" aria-hidden="true">
    <polygon points="0,740 47,730 47,768 0,776" fill="var(--brand-light)"/>
    <polygon points="0,776 47,768 47,800 0,800" fill="var(--brand-dark)"/>
    <polygon points="198,766 566,624 566,642 198,782" fill="var(--brand-light)"/>
    <polygon points="47,698 113,735 113,800 47,800" fill="var(--brand-mid)"/>
    <polygon points="113,735 198,702 198,782 566,642 566,800 113,800" fill="var(--brand-dark)"/>
  </svg>
  <div class="contact">22 Ridge Road Leederville, Western Australia<br>www.klvapartners.com.au<br>Ph: 08 6100 2200 • Fax: 08 6100 2299</div>
</section>

<section class="sheet comp-slip">
  <svg class="band" viewBox="0 0 565 265" aria-hidden="true">
    <polygon points="0,246 36,238 36,256 0,262" fill="var(--brand-light)"/>
    <polygon points="0,262 36,256 36,265 0,265" fill="var(--brand-dark)"/>
    <polygon points="173,218 565,86 565,100 173,232" fill="var(--brand-light)"/>
    <polygon points="36,173 96,203 96,265 36,265" fill="var(--brand-mid)"/>
    <polygon points="96,203 173,175 173,232 565,100 565,265 96,265" fill="var(--brand-dark)"/>
  </svg>
  <div class="wordmark"><span class="mark"></span>KLVA Partners</div>
  <h2 class="comp-title">WITH COMPLIMENTS</h2>
  <div class="contact">22 Ridge Road Leederville, Western Australia<br>www.klvapartners.com.au<br>Ph: 08 6100 2200 • Fax: 08 6100 2299</div>
</section>

<section class="sheet card-front">
  <svg class="band" viewBox="0 0 243 147" aria-hidden="true">
    <polygon points="0,125 15,120 15,133 0,137" fill="var(--brand-light)"/>
    <polygon points="0,137 15,133 15,147 0,147" fill="var(--brand-dark)"/>
    <polygon points="88,116 243,69 243,81 88,128" fill="var(--brand-light)"/>
    <polygon points="15,98 48,112 48,147 15,147" fill="var(--brand-mid)"/>
    <polygon points="48,112 88,97 88,128 243,81 243,147 48,147" fill="var(--brand-dark)"/>
  </svg>
  <div class="wordmark"><span class="mark"></span>KLVA Partners</div>
  <p class="offices">DARWIN • HOBART • OSAKA</p>
</section>

<section class="sheet card-back">
  <div class="card-art" role="img" aria-label="Isometric block illustration in blue tones"></div>
  <h3 class="holder-name">DANIEL REEVES</h3>
  <p class="holder-role">Australian Director</p>
  <div class="card-rule"></div>
  <div class="contact">22 Ridge Road Leederville, Western Australia • www.klvapartners.com.au<br>Ph: 08 6100 2200 • Fax: 08 6100 2299 • Mobile: 0400 555 123</div>
</section>

</body>
</html>
```